Marnie's Fitness Business Cards

I would like my business cards to look expensive and sophisticated using my logo and the information below.

FRONT
Marnie’s Fitness logo

Tag line Become your happiest, healthiest and strongest self

Marnie Pulham Crisp
Personal Trainer

e. marnie@marniesfitness.example

t. 0781350462

w. www.marniesfitness.example

```html
<!DOCTYPE html>
<html lang="en">
<head>
<meta charset="utf-8">
<title>Marnie's Fitness Business Cards</title>
<link rel="stylesheet" href="https://fonts.googleapis.com/css2?family=Open+Sans:wght@400;600&display=swap">
<style>
  :root {
    --backdrop: #7d797a;
    --card-white: #ffffff;
    --card-black: #000000;
    --teal: #67b4bb;
    --mauve: #a59391;
    --ink: #1c1c1c;
  }
  * { margin: 0; padding: 0; box-sizing: border-box; }
  html, body { width: 1200px; height: 900px; overflow: hidden; }
  body {
    background: var(--backdrop);
    font-family: "Open Sans", Arial, sans-serif;
    position: relative;
  }
  .card {
    position: absolute;
    top: 307px;
    width: 438px;
    height: 270px;
    border-radius: 11px;
    overflow: hidden;
  }
  .card--front { left: 150px; background: var(--card-white); }
  .card--back { left: 609px; background: var(--card-black); }

  .brand-name {
    position: absolute;
    left: 18px;
    top: 78px;
    width: 170px;
    text-align: center;
    color: var(--mauve);
    font-weight: 600;
    font-size: 21px;
    line-height: 1.25;
  }
  .brand-dot {
    position: absolute;
    left: 93px;
    top: 58px;
    width: 16px;
    height: 16px;
    border-radius: 50%;
    background: var(--teal);
  }
  .divider {
    position: absolute;
    left: 191px;
    top: 65px;
    width: 1px;
    height: 110px;
    background: #c9c3c2;
  }
  .details { position: absolute; left: 205px; top: 67px; }
  .details__name {
    color: var(--teal);
    font-size: 16.5px;
    font-weight: 400;
    letter-spacing: 0.2px;
    line-height: 22px;
  }
  .details__role {
    color: var(--mauve);
    font-size: 13px;
    line-height: 18px;
    margin-bottom: 8px;
  }
  .contact-list { list-style: none; }
  .contact-list li {
    display: flex;
    align-items: center;
    gap: 6px;
    color: var(--ink);
    font-size: 13px;
    line-height: 18px;
  }
  .contact-list svg { width: 12px; height: 12px; flex: none; }

  .tagline-band {
    position: absolute;
    left: 0;
    top: 214px;
    width: 100%;
    height: 38px;
    background: var(--teal);
    color: #fff;
    font-weight: 600;
    font-size: 14.5px;
    text-align: center;
    line-height: 38px;
  }

  .back-dot {
    position: absolute;
    left: 211px;
    top: 130px;
    width: 16px;
    height: 16px;
    border-radius: 50%;
    background: var(--teal);
  }
  .back-brand {
    position: absolute;
    left: 0;
    top: 168px;
    width: 100%;
    text-align: center;
    color: var(--teal);
    font-size: 28px;
    font-weight: 400;
    letter-spacing: 5px;
    text-transform: uppercase;
    line-height: 1.1;
  }
</style>
</head>
<body>
  <section class="card card--front">
    <span class="brand-dot"></span>
    <p class="brand-name">Marnie’s<br>Fitness</p>
    <span class="divider"></span>
    <div class="details">
      <h1 class="details__name">MARNIE PULHAM CRISP</h1>
      <p class="details__role">Personal Trainer</p>
      <ul class="contact-list">
        <li>
          <svg viewBox="0 0 12 12" aria-hidden="true"><rect width="12" height="12" rx="2" fill="#67b4bb"/><rect x="3.8" y="2" width="4.4" height="8" rx="0.8" fill="none" stroke="#1c1c1c" stroke-width="1"/></svg>
          0781350462
        </li>
        <li>
          <svg viewBox="0 0 12 12" aria-hidden="true"><rect width="12" height="12" rx="2" fill="#67b4bb"/><rect x="2.5" y="3.5" width="7" height="5" fill="#1c1c1c"/><path d="M2.5 3.5 6 6.5 9.5 3.5" fill="none" stroke="#67b4bb" stroke-width="0.8"/></svg>
          marnie@marniesfitness.example
        </li>
        <li>
          <svg viewBox="0 0 12 12" aria-hidden="true"><rect width="12" height="12" rx="2" fill="#67b4bb"/><circle cx="6" cy="6" r="3.6" fill="#1c1c1c"/><path d="M2.4 6h7.2M6 2.4c-1.6 2-1.6 5.2 0 7.2M6 2.4c1.6 2 1.6 5.2 0 7.2" fill="none" stroke="#67b4bb" stroke-width="0.6"/></svg>
          www.marniesfitness.example
        </li>
      </ul>
    </div>
    <p class="tagline-band">Become your happiest, healthiest and strongest self</p>
  </section>

  <section class="card card--back">
    <span class="back-dot"></span>
    <p class="back-brand">Marnie’s<br>Fitness</p>
  </section>
</body>
</html>
```